Plakate für Haushaltshilfen und Alltagsbegleiter
Zielgruppe
Wir bieten haushaltsnahe Dienstleistungen (Haushaltshilfen und Altgasbegleiter) für Personen mit einem Pflegegrad 1 - 5 an.
Zielgruppe sind Personen mit einem Pflegegrad 1 - 5. Hauptsächlich ältere Menschen die Unterstützung/Betreuung im Alltag und Haushalt benötigen.
Aufgabenstellung
Wir benötigen für unsere Büroräume eine Fensterbeschriftung. Es handelt sich hier um 5 Fenster (Glasflächen) und eine Glastür. Die Vorgabe ist, dass von außen zu erkennen ist dass sich um alle Räumlichkeiten um unsere (Firma Lindwerk) Räumlichkeiten handelt. Desweiteren soll auch unser Angebot erkennbar sein.
Unser Angebot enthält: Haushaltshilfen und Alltagsbegleiter
- kostenlose Haushaltshilfe ab Pflegegrad 1
- Abrechnung mit allen Kostenträgern
Da wir keine Schilder an die Fassade anbringen können, müßen die Glasflächen dafür genutzt werden um zum Einen uns als Firma erkennbar zu machen und zum anderen unser Angebot kurz zu präsentieren.
Uns ist wichtig dass unser Logo verwendet wir und auch unsere Farben.
Desweiteren sollten an den Fenstern auch teilweise eine Sichtschutz nach innen, angebracht werden, aber eben nur teilweise also nicht das ganzen Fenster z.Bsp. mit einer Blickdichten Folie überziehen, sondern in Augenhöhe wenn Fußgänger vorbei laufen.

```html
<!DOCTYPE html>
<html lang="de">
<head>
<meta charset="utf-8">
<title>Lindwerk – Fensterbeschriftung</title>
<link href="https://fonts.googleapis.com/css2?family=Rubik:wght@400;500;700&family=Gochi+Hand&display=swap" rel="stylesheet">
<style>
:root{
  --stage:#6b6b6b;
  --paper:#e7e7e7;
  --paper-2:#d6d6d6;
  --red:#d10d0d;
  --red-dark:#8f0c0c;
  --dark:#353535;
  --slate:#5e5e5e;
  --white:#ffffff;
}
*{margin:0;padding:0;box-sizing:border-box}
html,body{width:1200px;height:733px;overflow:hidden;background:var(--stage);font-family:"Rubik",sans-serif}
.stage{position:relative;width:1200px;height:733px}
.poster{position:absolute;overflow:hidden;background:linear-gradient(160deg,var(--paper) 0%,var(--paper-2) 100%)}
.poster svg.bands{position:absolute;left:0;bottom:0;width:100%;height:auto;display:block}
.brand{position:absolute;display:flex;align-items:center;gap:7px}
.brand-dot{width:26px;height:26px;border-radius:50%;border:3px solid var(--red);flex:none}
.brand-name{font-family:"Rubik",sans-serif;font-weight:500;font-size:17px;letter-spacing:1px;color:var(--dark)}
.on-dark .brand-name{color:var(--white)}
.script{font-family:"Gochi Hand",cursive;color:var(--red)}
.headline{font-weight:700;text-transform:uppercase;text-align:center;line-height:1.3}

/* poster 1 – Vorteile */
.p-vorteile{left:40px;top:238px;width:181px;height:245px}
.p-vorteile .tagline{position:absolute;right:18px;top:54px;font-size:10px}
.p-vorteile .bar{position:absolute;left:0;top:74px;width:100%;height:17px;background:var(--dark);color:var(--white);font-size:10px;display:flex;align-items:center;justify-content:center}
.benefit{position:absolute;width:80px;text-align:center;font-size:5.6px;color:#444;line-height:1.25}
.benefit .icon{width:28px;height:28px;margin:0 auto 3px;background:var(--red);border-radius:4px;display:flex;align-items:center;justify-content:center}
.benefit .icon svg{width:16px;height:16px}

/* poster 2 – Foto */
.p-foto{left:230px;top:238px;width:181px;height:245px}
.p-foto .photo{position:absolute;left:0;top:0;width:100%;height:190px;background:linear-gradient(135deg,#f2f2f2 0%,#cfcfcf 55%,#9a9a9a 100%)}
.p-foto .footer-text{position:absolute;left:0;bottom:9px;width:100%;color:var(--white);font-size:8.6px}

/* poster 3 – Entlastungsbetrag */
.p-betrag{left:422px;top:238px;width:180px;height:245px}
.p-betrag .headline{position:absolute;left:10px;right:10px;top:96px;color:var(--red);font-size:9px}

/* poster 4 – Kontakt */
.p-kontakt{left:614px;top:216px;width:180px;height:290px;background:var(--slate)}
.p-kontakt .top{position:absolute;left:0;top:0;width:100%;height:150px;background:linear-gradient(170deg,var(--paper),var(--paper-2));clip-path:polygon(0 0,100% 0,100% 80%,50% 100%,0 80%)}
.p-kontakt .photo{position:absolute;left:0;top:56px;width:100%;height:94px;background:linear-gradient(120deg,#f4f4f4 0%,#bdbdbd 50%,#efefef 100%);clip-path:polygon(0 0,100% 0,100% 60%,50% 100%,0 60%)}
.p-kontakt .invite{position:absolute;left:0;top:163px;width:100%;text-align:center;color:var(--white);font-size:9px;line-height:1.3}
.p-kontakt .phone{position:absolute;left:15px;right:17px;top:190px;height:22px;background:var(--red);border-radius:6px;color:var(--white);font-weight:700;font-size:14px;letter-spacing:.5px;display:flex;align-items:center;justify-content:center}
.p-kontakt .web{position:absolute;left:0;top:219px;width:100%;text-align:center;color:var(--white);font-size:13.5px;font-weight:500}

/* poster 5 – Tür */
.p-tuer{left:816px;top:190px;width:143px;height:318px;background:var(--slate)}
.p-tuer .tagline{position:absolute;left:30px;top:78px;font-size:11px;transform:rotate(14deg);transform-origin:left center}
.p-tuer .mark{position:absolute;left:42px;top:102px;width:58px;height:58px;border-radius:50%;border:5px solid var(--red)}
.p-tuer .door-name{position:absolute;left:0;top:164px;width:100%;text-align:center;font-weight:500;font-size:17px;letter-spacing:1px;color:var(--white)}

/* poster 6 – Pflegegrad */
.p-pflegegrad{left:981px;top:216px;width:180px;height:290px;background:var(--slate)}
.p-pflegegrad .headline{position:absolute;left:0;width:100%;top:96px;color:var(--white);font-size:12.5px;line-height:1.35}
.p-pflegegrad .tag{position:absolute;left:42px;top:166px;width:116px;height:38px;background:var(--red);border-radius:7px;transform:rotate(-14deg);color:var(--white);font-weight:700;font-size:7.6px;line-height:1.2;text-align:center;display:flex;align-items:center;justify-content:center;text-transform:uppercase}

.cut-lines{position:absolute;left:0;top:0;width:1200px;height:733px;pointer-events:none}
.cut-label{position:absolute;left:790px;top:516px;color:var(--white);font-size:21px;letter-spacing:.5px;font-weight:400}
</style>
</head>
<body>
<div class="stage">

  <!-- Vorteile -->
  <section class="poster p-vorteile">
    <div class="brand" style="left:18px;top:18px"><span class="brand-dot"></span><span class="brand-name">LINDWERK</span></div>
    <div class="script tagline">Wir sind für Sie da!</div>
    <div class="bar headline">Unsere Vorteile</div>
    <div class="benefit" style="left:7px;top:99px"><div class="icon"><svg viewBox="0 0 16 16"><path d="M4 1h6l3 3v11H4z" fill="#fff"/></svg></div>Abrechnung mit allen<br>Pflegekassen möglich</div>
    <div class="benefit" style="left:90px;top:99px"><div class="icon"><svg viewBox="0 0 16 16"><path d="M7 2h2v3h3v2H9v3H7V7H4V5h3z M1 12h14v2H1z" fill="#fff"/></svg></div>Entlastungsbetrag<br>von mind. 125 € mtl.<br>ab Pflegegrad 1</div>
    <div class="benefit" style="left:7px;top:160px"><div class="icon"><svg viewBox="0 0 16 16"><path d="M8 11 3 6a2.5 2.5 0 0 1 5-2 2.5 2.5 0 0 1 5 2z M1 13h14v2H1z" fill="#fff"/></svg></div>Verhinderungspflege<br>ab Pflegegrad 2</div>
    <div class="benefit" style="left:90px;top:160px"><div class="icon"><svg viewBox="0 0 16 16"><path d="M3 1h7v14H3z" fill="#fff"/><path d="M9 12l5-6 1 1-5 6z" fill="#fff"/></svg></div>Hilfe bei der<br>Antragsstellung</div>
    <svg class="bands" viewBox="0 0 181 60"><polygon points="0,14 80,56 181,8 181,60 0,60" fill="var(--red)"/><polygon points="0,14 80,56 72,60 0,60" fill="var(--red-dark)"/><polygon points="120,60 181,30 181,60" fill="var(--dark)"/></svg>
  </section>

  <!-- Foto -->
  <section class="poster p-foto">
    <div class="photo" role="img" aria-label="Schwarzweißfoto: ältere Hände auf einem Gehstock, von einer helfenden Hand gehalten"></div>
    <div class="brand" style="left:18px;top:18px"><span class="brand-dot"></span><span class="brand-name">LINDWERK</span></div>
    <svg class="bands" viewBox="0 0 181 85"><polygon points="0,15 60,8 181,25 181,85 0,85" fill="var(--dark)"/><polygon points="0,15 60,8 135,22 181,0 181,12 130,34 55,22 0,32" fill="var(--red)"/><polygon points="0,15 55,18 0,32" fill="var(--red-dark)"/></svg>
    <div class="footer-text headline">Haushaltshilfen und<br>Altagsbegleitung<br>ab Pflegegrad 1</div>
  </section>

  <!-- Entlastungsbetrag -->
  <section class="poster p-betrag">
    <div class="brand" style="left:18px;top:18px"><span class="brand-dot"></span><span class="brand-name">LINDWERK</span></div>
    <div class="headline">Nutzen Sie Ihren<br>Entlastungsbetrag<br>ab Pflegegrad 1 und Ihre<br>Verhinderungspflege<br>ab dem Pflegegrad 2,<br>bevor der Anspruch<br>verfällt</div>
    <svg class="bands" viewBox="0 0 180 60"><polygon points="0,14 80,56 180,8 180,60 0,60" fill="var(--red)"/><polygon points="0,14 80,56 72,60 0,60" fill="var(--red-dark)"/><polygon points="120,60 180,30 180,60" fill="var(--dark)"/></svg>
  </section>

  <!-- Kontakt -->
  <section class="poster p-kontakt on-dark">
    <div class="top"></div>
    <div class="photo" role="img" aria-label="Schwarzweißfoto: eine Hand hält sanft eine ältere Hand"></div>
    <div class="brand" style="left:18px;top:16px"><span class="brand-dot"></span><span class="brand-name" style="color:var(--dark)">LINDWERK</span></div>
    <p class="invite">Buchen Sie gleich hier einen<br>Termin oder rufen Sie uns unter</p>
    <div class="phone">0711 62 38 07 19</div>
    <div class="web">www.lindwerk.de</div>
    <svg class="bands" viewBox="0 0 180 60"><polygon points="0,18 65,38 180,0 180,60 0,60" fill="var(--red)"/><polygon points="0,18 65,38 60,60 0,60" fill="var(--red-dark)"/><polygon points="100,60 180,32 180,60" fill="#3a3a3a"/></svg>
  </section>

  <!-- Tür -->
  <section class="poster p-tuer on-dark">
    <svg class="bands" viewBox="0 0 143 72" style="top:0;bottom:auto"><polygon points="0,0 113,0 0,72" fill="var(--red)"/><polygon points="113,0 143,0 143,42 100,24" fill="#f3f3f3"/><polygon points="20,46 100,24 40,50" fill="var(--red-dark)"/></svg>
    <div class="script tagline">Wir sind für Sie da!</div>
    <div class="mark"></div>
    <div class="door-name">LINDWERK</div>
    <svg class="bands" viewBox="0 0 143 52"><polygon points="0,6 70,16 143,0 143,52 0,52" fill="var(--red)"/><polygon points="0,20 60,26 112,36 143,26 143,52 0,52" fill="#ffffff"/><polygon points="0,6 40,10 0,20" fill="var(--red-dark)"/></svg>
  </section>

  <!-- Pflegegrad -->
  <section class="poster p-pflegegrad on-dark">
    <div class="brand" style="left:18px;top:18px"><span class="brand-dot"></span><span class="brand-name">LINDWERK</span></div>
    <div class="headline">Haushaltshilfe<br>ab Pflegegrad 1</div>
    <div class="tag">Abrechnung mit<br>allen Pflegekassen<br>möglich</div>
    <svg class="bands" viewBox="0 0 180 60"><polygon points="0,18 78,46 180,0 180,60 0,60" fill="var(--red)"/><polygon points="0,18 78,46 70,60 0,60" fill="var(--red-dark)"/><polygon points="110,60 180,30 180,60" fill="#3a3a3a"/></svg>
  </section>

  <svg class="cut-lines" viewBox="0 0 1200 733">
    <g stroke="#ffffff" stroke-width=".7" fill="none">
      <line x1="760" y1="520" x2="668" y2="470"/>
      <line x1="815" y1="518" x2="760" y2="360"/>
      <line x1="820" y1="518" x2="845" y2="475"/>
      <line x1="830" y1="518" x2="875" y2="360"/>
      <line x1="900" y1="518" x2="1010" y2="390"/>
      <line x1="905" y1="518" x2="1020" y2="440"/>
      <line x1="910" y1="518" x2="1000" y2="470"/>
    </g>
  </svg>
  <div class="cut-label">KONTURSCHNEIDEN</div>
</div>
</body>
</html>
```